Roadward Lane Management Company Website

Modern website Wordpress design using all greyscale photos with a pop of red (such as road closure signs or detour cones) for strategic emphasis. (see brand guide for color codes)
The creative goal is to leverage high-contrast, desaturated imagery to create a clean, professional, and industrial feel. The selective use of red will draw immediate attention to critical elements—such as road hazards, safety equipment, or key messages to ensure the viewer's focus is directed with purpose.

Brand guide, homepage content and logo are attached. Create clean professional user experience to market services to industry professionals.

```html
<!DOCTYPE html>
<html lang="en">
<head>
<meta charset="utf-8">
<title>Roadward Lane Management Company</title>
<link href="https://fonts.googleapis.com/css2?family=Roboto+Condensed:wght@400;500;700&family=Inter:wght@400;500;600&display=swap" rel="stylesheet">
<style>
:root{
  --red:#e61e25;
  --red-dark:#9b1016;
  --black:#000;
  --ink:#0f0f10;
  --charcoal:#2b2d31;
  --grey:#555;
  --light:#f0f0f0;
  --white:#fff;
  --shadow:#3a3a3a;
}
*{margin:0;padding:0;box-sizing:border-box}
html,body{width:1200px;height:3424px;overflow:hidden;background:var(--black)}
body{position:relative;font-family:Inter,Arial,sans-serif;color:var(--white)}
.abs{position:absolute}
.head{font-family:"Roboto Condensed",Arial,sans-serif}
.btn{position:absolute;background:var(--red);color:var(--white);font-family:"Roboto Condensed",Arial,sans-serif;font-weight:700;font-size:14px;display:flex;align-items:center;justify-content:center;text-transform:uppercase;box-shadow:6px 6px 0 var(--shadow)}
.btn-outline{position:absolute;border:3px solid var(--red);color:var(--charcoal);background:var(--white);font-family:"Roboto Condensed",Arial,sans-serif;font-weight:700;font-size:13px;display:flex;align-items:center;justify-content:center;box-shadow:5px 5px 0 #bdbdbd}
.brand{display:flex;align-items:center;gap:10px;font-family:"Roboto Condensed",Arial,sans-serif;font-weight:700;font-size:32px;color:var(--white)}
.brand i{width:18px;height:18px;background:var(--red);display:block}

/* hero */
.hero-bg{position:absolute;left:0;top:0;width:1200px;height:1010px;background:radial-gradient(ellipse at 70% 35%,#5a1016 0%,#2a0a0c 30%,#111 60%,#050505 100%)}
.hero-band{position:absolute;left:0;top:330px;width:1200px;height:260px;background:linear-gradient(170deg,transparent 20%,rgba(200,20,30,.35) 50%,transparent 80%)}
.site-header{position:absolute;left:0;top:0;width:1200px;height:120px;z-index:5}
.nav{position:absolute;left:0;top:62px;font-family:"Roboto Condensed",Arial,sans-serif;font-size:14px;text-transform:uppercase;color:var(--white)}
.nav span{position:absolute;white-space:nowrap}
.hero-title{position:absolute;left:110px;top:170px;font-family:"Roboto Condensed",Arial,sans-serif;font-weight:700;font-size:58px;line-height:62px}
.hero-sub{position:absolute;left:280px;top:310px;font-family:"Roboto Condensed",Arial,sans-serif;font-size:20px}
.motto{position:absolute;left:110px;top:670px;font-family:"Roboto Condensed",Arial,sans-serif;font-size:50px;line-height:77px;text-transform:uppercase}
.badge{position:absolute;border-radius:50%}
.badge-label{position:absolute;font-family:"Roboto Condensed",Arial,sans-serif;font-size:17px;text-align:center;width:220px}

/* about */
.about{position:absolute;left:0;top:1010px;width:1200px;height:573px;background:var(--black)}
.about-frame{position:absolute;left:70px;top:1090px;width:580px;height:320px;border:1px solid var(--red-dark);transform:rotate(-12deg);background:#111}
.about-photo{position:absolute;left:110px;top:1090px;width:498px;height:330px;background:linear-gradient(180deg,#9a9a9a,#3b3b3b 60%,#1a1a1a)}
.eyebrow{font-family:Inter,Arial,sans-serif;color:var(--red);font-size:25px;font-weight:500}
.about-copy{position:absolute;left:710px;top:1088px;width:392px}
.about-copy h2{font-family:"Roboto Condensed",Arial,sans-serif;font-weight:400;font-size:30px;line-height:36px;margin-top:4px}
.about-copy p{font-size:12px;line-height:29px;margin-top:18px;letter-spacing:-.1px}
.about-copy b{color:var(--red);font-weight:600}

/* services */
.services{position:absolute;left:0;top:1583px;width:1200px;height:829px;background:var(--white);color:var(--charcoal)}
.center{position:absolute;left:0;width:1200px;text-align:center}
.card{position:absolute;top:206px;width:308px;height:540px;border:2px solid var(--red);background:var(--white)}
.card-img{position:absolute;left:0;top:0;width:304px;height:255px;background:#000}
.card-label{position:absolute;left:32px;top:218px;width:243px;height:75px;display:flex}
.card-label .ico{width:75px;background:var(--charcoal);display:flex;align-items:center;justify-content:center}
.card-label .txt{flex:1;background:var(--red);color:var(--white);font-size:15px;font-weight:600;line-height:24px;padding:13px 16px}
.card p{position:absolute;left:22px;top:317px;width:260px;text-align:center;font-size:17px;line-height:34px;color:var(--grey)}
.card .btn-outline{left:85px;top:444px;width:135px;height:43px}

/* industry */
.industry{position:absolute;left:0;top:2412px;width:1200px;height:638px;background:var(--ink)}
.map{position:absolute;left:410px;top:30px;width:400px;height:440px;background:radial-gradient(ellipse,rgba(230,30,37,.12),transparent 70%)}
.bullet{position:absolute;font-size:20px;display:flex;align-items:center;gap:12px}
.bullet:before{content:"";width:8px;height:8px;border-radius:50%;background:var(--white)}
.feat{position:absolute;width:260px;text-align:center;font-size:17px}
.feat svg{display:block;margin:0 auto 16px}

/* footer */
.footer{position:absolute;left:0;top:3050px;width:1200px;height:374px;background:var(--white);color:var(--charcoal)}
.footer .brand{color:var(--black);position:absolute;left:110px;top:62px}
.foot-text{position:absolute;left:110px;top:172px;width:330px;font-size:15px;line-height:29px}
.col{position:absolute;top:95px}
.col h4{font-family:"Roboto Condensed",Arial,sans-serif;font-weight:500;font-size:19px;margin-bottom:22px;color:var(--charcoal)}
.col li{list-style:none;font-size:15px;line-height:29px}
.certs{position:absolute;left:910px;top:68px;width:210px;height:255px;background:var(--light);padding:36px 36px}
.certs h4{font-family:"Roboto Condensed",Arial,sans-serif;font-weight:500;font-size:19px}
.cert{display:flex;align-items:center;gap:18px;margin-top:26px;font-size:16px}
.cert span{width:56px;height:56px;border-radius:50%;display:block}
.copy{position:absolute;top:340px;left:0;width:1200px;text-align:center;font-size:11px}
</style>
</head>
<body>

<div class="hero-bg" role="img" aria-label="Greyscale night highway curving through a valley, lined with glowing red barriers and traffic cones"></div>
<div class="hero-band"></div>

<header class="site-header">
  <div class="brand abs" style="left:112px;top:44px"><i></i>Roadward</div>
  <nav class="nav">
    <span style="left:360px">Home</span>
    <span style="left:435px">About</span>
    <span style="left:516px">Services</span>
    <span style="left:616px">Rentals</span>
    <span style="left:710px">Jobs</span>
    <span style="left:782px">Contact</span>
  </nav>
  <div class="btn" style="left:953px;top:45px;width:137px;height:45px">Get in touch</div>
</header>

<h1 class="hero-title">Traffic Control Solutions<br>Engineered For Safety.</h1>
<p class="hero-sub">Specialized solutions to keep roads safe and compliant.</p>
<div class="btn" style="left:111px;top:405px;width:137px;height:45px">Get started</div>

<p class="motto">Safety isn’t a priority,<br>it’s the foundation of<br>everything we do.</p>
<div class="badge" style="left:682px;top:670px;width:180px;height:180px;background:radial-gradient(circle,#d8a640 0%,#7a5a18 60%,#2a2a2a 62%,#111 100%)" role="img" aria-label="Safety association certification seal"></div>
<div class="badge" style="left:913px;top:676px;width:168px;height:168px;background:radial-gradient(circle,#9a8572,#6a5545 70%,#3d2f26 100%)" role="img" aria-label="State transportation department certification seal"></div>
<div class="badge-label" style="left:662px;top:858px">NRSA Certified</div>
<div class="badge-label" style="left:887px;top:858px">StateDOT-Compliant &amp; Certified</div>

<section class="about"></section>
<div class="about-frame"></div>
<div class="about-photo" role="img" aria-label="Greyscale photo of two red traffic cones on cracked asphalt"></div>
<div class="about-copy">
  <div class="eyebrow">About Us</div>
  <h2>Commitment to Safety,<br>Compliance &amp; Efficiency</h2>
  <p>For years, <b>Roadward</b> has been a leader in traffic control solutions across Texas. We specialize in providing reliable, certified, and compliant traffic control services for road construction, municipal projects, private contractors, and industrial sectors. With a highly trained crew and a dedication to safety, we help ensure that every project runs smoothly, efficiently, and in full compliance with StateDOT and WSHA regulations.</p>
</div>
<div class="btn" style="left:711px;top:1442px;width:135px;height:45px">Learn more</div>

<section class="services">
  <div class="center eyebrow" style="top:82px">Services We Offer</div>
  <div class="center head" style="top:128px;font-size:29px">Tailored Traffic Control Solutions for Any Project</div>

  <svg class="abs" style="left:42px;top:440px" width="28" height="44" viewBox="0 0 28 44"><path d="M24 2 4 22l20 20" fill="none" stroke="#333" stroke-width="3"/></svg>
  <svg class="abs" style="left:1128px;top:440px" width="28" height="44" viewBox="0 0 28 44"><path d="M4 2l20 20L4 42" fill="none" stroke="#333" stroke-width="3"/></svg>

  <div class="card" style="left:110px">
    <div class="card-img" role="img" aria-label="Orange road work ahead diamond sign on black"></div>
    <div class="card-label"><div class="ico"><svg width="40" height="40" viewBox="0 0 40 40" fill="none" stroke="#fff" stroke-width="2"><path d="M8 34 30 8M32 34 10 8M22 6l10 4-4 6zM18 6 8 10l4 6z"/></svg></div><div class="txt">Flagging &amp; Lane Closures</div></div>
    <p>Trained flaggers and coordinated lane closures to minimize traffic disruptions.</p>
    <div class="btn-outline">VIEW SERVICE</div>
  </div>
  <div class="card" style="left:445px">
    <div class="card-img" role="img" aria-label="Yellow diverted traffic sign on black"></div>
    <div class="card-label"><div class="ico"><svg width="42" height="30" viewBox="0 0 42 30" fill="none" stroke="#fff" stroke-width="2"><rect x="3" y="5" width="36" height="16"/><path d="M9 5v16M15 5v16M21 5v16M27 5v16M33 5v16M6 21v7M36 21v7"/></svg></div><div class="txt">Signage &amp; Barricades</div></div>
    <p>High-quality road signs, barricades, and warning systems for work zones.</p>
    <div class="btn-outline">VIEW SERVICE</div>
  </div>
  <div class="card" style="left:779px">
    <div class="card-img" role="img" aria-label="Orange traffic cone on black"></div>
    <div class="card-label"><div class="ico"><svg width="34" height="40" viewBox="0 0 34 40" fill="none" stroke="#fff" stroke-width="2"><path d="M14 4h6l10 30H4zM10 18h14M7 27h20M2 36h30"/></svg></div><div class="txt">Event Traffic &amp; Crowd Control</div></div>
    <p>Secure traffic planning for major public gatherings and help regulate traffic.</p>
    <div class="btn-outline">VIEW SERVICE</div>
  </div>
</section>

<section class="industry">
  <div class="map" role="img" aria-label="Faint dotted outline map of Texas"></div>
  <div class="center eyebrow" style="top:85px">Serving Texas Industry</div>
  <div class="center head" style="top:138px;font-size:30px">We Ensure Safety, Compliance, and Efficient Traffic Flow</div>
  <div class="bullet" style="left:184px;top:203px">Road construction, maintenance, &amp; Detours</div>
  <div class="bullet" style="left:664px;top:203px">Municipal &amp; State projects</div>
  <div class="bullet" style="left:184px;top:255px">Private Sector &amp; Commercial Contractors</div>
  <div class="bullet" style="left:664px;top:255px">Oil, Gas, Wind, Solar, &amp; Manufacturing</div>

  <div class="feat" style="left:158px;top:315px">
    <svg width="80" height="72" viewBox="0 0 80 72" fill="none" stroke="#e61e25" stroke-width="3"><circle cx="24" cy="14" r="8"/><path d="M10 66V36q0-8 14-8t14 8v30M18 66V46M30 66V46"/><circle cx="58" cy="44" r="12"/><path d="M52 44l5 5 8-9"/></svg>
    Experienced &amp; Trained Crew
  </div>
  <div class="feat" style="left:470px;top:315px">
    <svg width="70" height="72" viewBox="0 0 70 72" fill="none" stroke="#e61e25" stroke-width="3"><path d="M35 3 62 14v20q0 22-27 35Q8 56 8 34V14z"/><path d="M24 44V30h6l6-10q4 0 3 8h8v16H24"/><circle cx="54" cy="56" r="9" fill="#e61e25"/></svg>
    Reliable &amp; Responsive
  </div>
  <div class="feat" style="left:783px;top:315px">
    <svg width="80" height="72" viewBox="0 0 80 72" fill="#e61e25"><path d="M44 4h20l-4 10H48z"/><path d="M42 18h24q12 14 12 30 0 20-24 20T30 48q0-16 12-30z"/><path d="M6 40h24v6H6zM2 52h28v6H2zM10 62h22v6H10z"/><text x="48" y="54" fill="#0f0f10" font-family="Arial" font-weight="700" font-size="22">$</text></svg>
    Cost-Effective &amp; Efficient
  </div>
  <div class="btn" style="left:532px;top:500px;width:135px;height:45px">Get started</div>
</section>

<footer class="footer">
  <div class="brand"><i></i>Roadward</div>
  <p class="foot-text">With a highly trained crew and a dedication to safety, we help ensure that every project runs smoothly, efficiently, and in full compliance with StateDOT and WSHA regulations.</p>
  <div class="col" style="left:521px"><h4>NAVIGATION</h4><ul><li>Home</li><li>About</li><li>Services</li><li>Rentals</li><li>Job Contact</li></ul></div>
  <div class="col" style="left:711px"><h4>USEFUL LINKS</h4><ul><li>Support</li><li>Terms of Sercice</li><li>Cookies</li><li>Get in Touch</li><li>Privacy</li></ul></div>
  <div class="certs">
    <h4>CERTIFICATIONS</h4>
    <div class="cert"><span style="background:radial-gradient(circle,#c99a3a,#6b4f15)"></span>NRSA</div>
    <div class="cert"><span style="background:radial-gradient(circle,#b8a898,#7a6555)"></span>StateDOT</div>
  </div>
  <div class="copy">Copyright © 2025 Roadward. All rights reserved.</div>
</footer>

</body>
</html>
```